Simple but elegant business card/logo design for exclusive beauty business

We need a logo designed for a new elegant and exclusive beauty business called "R". The logo itself should be a stylistic and custom design for the letter "R". We would like the business card to have the logo as the centrepiece on a clean background. Gold Logo on black background or silver on white background.

The business card details should be displayed centre of the card. Details are as follows:

Tamsin Earle
Facebook: /shinesoftlyr
Instagram: /shinesoftlyr

The words "Shine Softly" should also appear somewhere on the card.

Industry/Entity Type

Business

Logo Text

G

Requirements
Must have
• Design must be simple, clean and elegant
Should not have
• The design should not be cluttered

```html
<!DOCTYPE html>
<html lang="en">
<head>
<meta charset="utf-8">
<title>Tamsin Earle – Business Card</title>
<link rel="stylesheet" href="https://fonts.googleapis.com/css2?family=Raleway:wght@400&family=Cinzel:wght@500&family=Tinos&family=Pinyon+Script&display=swap">
<style>
  :root {
    --backdrop: #1c1c1c;
    --card: #131313;
    --gold: #d9b24a;
    --gold-line: #b8953a;
    --white: #f4f4f4;
  }
  html, body {
    margin: 0;
    width: 1200px;
    height: 1200px;
    overflow: hidden;
    background: var(--backdrop);
  }
  .canvas {
    width: 1200px;
    height: 1200px;
    display: flex;
    flex-direction: column;
    align-items: center;
    justify-content: center;
    gap: 56px;
  }
  .card {
    position: relative;
    width: 860px;
    height: 480px;
    background: var(--card);
    box-shadow: 0 18px 40px rgba(0,0,0,0.55);
    display: flex;
    flex-direction: column;
    align-items: center;
  }
  .brand-mark {
    font-family: "Tinos", serif;
    font-weight: 400;
    color: var(--gold);
    line-height: 1;
  }
  /* Front */
  .card--front .brand-mark {
    margin-top: 78px;
    font-size: 150px;
  }
  .card--front .holder-name {
    margin-top: 16px;
    font-family: "Raleway", sans-serif;
    font-size: 34px;
    letter-spacing: 0.14em;
    color: var(--white);
  }
  .tagline-rule {
    position: absolute;
    left: 60px;
    right: 60px;
    bottom: 72px;
    display: flex;
    align-items: center;
    gap: 18px;
  }
  .tagline-rule .rule {
    flex: 1;
    height: 1px;
    background: var(--gold-line);
  }
  .tagline {
    font-family: "Pinyon Script", cursive;
    font-size: 34px;
    color: var(--gold);
  }
  /* Back */
  .card--back .brand-mark {
    margin-top: 62px;
    font-size: 170px;
  }
  .card--back .holder-name {
    margin-top: 18px;
    font-family: "Cinzel", serif;
    font-weight: 500;
    font-size: 38px;
    letter-spacing: 0.06em;
    color: var(--white);
  }
  .socials {
    margin-top: 14px;
    font-family: "Tinos", serif;
    font-size: 27px;
    color: var(--white);
    display: flex;
    align-items: center;
    gap: 22px;
  }
  .socials .label { color: var(--gold); }
  .socials .dot {
    width: 12px;
    height: 12px;
    border-radius: 50%;
    background: var(--gold);
  }
</style>
</head>
<body>
  <main class="canvas">
    <section class="card card--front">
      <div class="brand-mark">R</div>
      <div class="holder-name">TAMSIN EARLE</div>
      <div class="tagline-rule">
        <span class="rule"></span>
        <span class="tagline">Shine Softly</span>
        <span class="rule"></span>
      </div>
    </section>
    <section class="card card--back">
      <div class="brand-mark">R</div>
      <div class="holder-name">TAMSIN EARLE</div>
      <div class="socials">
        <span><span class="label">Facebook:</span> shinesoftlyr</span>
        <span class="dot"></span>
        <span><span class="label">Instagram:</span> shinesoftlyr</span>
      </div>
    </section>
  </main>
</body>
</html>
```